Harborline Security and Surveillance Business Card

Business Card Design - Company Name:Freedom Security and SurveillanceWe are a Security Systems Integrator Specializing in Security Systems/ Video Surveillance and Access Control. Our areas of expertise are:Security SystemsVideo SurveillanceAccess ControlFire Alarm SystemsNetwork CablingCellular BoostersMy input is the Front of the Card is: logo, name of Business, My Name, Phone Number, and email.Rear of Card is the 6 areas of expertise, I just dont want the front to be very busy.
Name: Glen Tavish
Title: President
Email: glen@harborlinesecsys.example
website: harborlinesecsys.example

```html
<!DOCTYPE html>
<html lang="en">
<head>
<meta charset="utf-8">
<title>Harborline Security and Surveillance – Business Card</title>
<link rel="stylesheet" href="https://fonts.googleapis.com/css2?family=Exo+2:wght@400;500;600;700&family=Roboto:wght@400;500&display=swap">
<style>
  :root {
    --page-bg: #e9e6e1;
    --card-black: #111214;
    --brand-blue: #2357a3;
    --panel-grey: #e4e5e7;
    --divider-grey: #eceef0;
    --ink-dark: #16171a;
    --ink-light: #ffffff;
    --silver-top: #f2f3f5;
    --silver-mid: #b9bcc1;
    --silver-low: #8e9197;
    --dash: #c9cbcf;
  }
  * { box-sizing: border-box; margin: 0; padding: 0; }
  html, body { width: 900px; height: 1200px; overflow: hidden; }
  body {
    background: var(--page-bg);
    position: relative;
    font-family: "Exo 2", sans-serif;
  }

  .card {
    position: absolute;
    left: 78px;
    width: 762px;
    border-radius: 20px;
    overflow: hidden;
    background: var(--card-black);
    box-shadow: 0 6px 16px rgba(0,0,0,.25);
  }

  /* Front */
  .card-front { top: 137px; height: 433px; }
  .brand {
    position: absolute;
    top: 70px; left: 92px;
    display: flex; align-items: center; gap: 22px;
  }
  .brand-mark {
    width: 70px; height: 70px;
    background: var(--brand-blue);
    border-radius: 50%;
    flex: none;
  }
  .brand-name {
    color: var(--brand-blue);
    font-weight: 600;
    font-size: 34px;
    letter-spacing: 5.5px;
    line-height: 1.05;
    text-transform: uppercase;
    white-space: nowrap;
  }
  .brand-name .brand-sub {
    display: block;
    font-size: 20px;
    letter-spacing: 16px;
    margin-top: 2px;
  }
  .front-divider {
    position: absolute;
    top: 220px; left: 0; right: 0; height: 11px;
    background: var(--divider-grey);
  }
  .name-panel {
    position: absolute;
    top: 231px; left: 0; width: 356px; bottom: 0;
    background: var(--brand-blue);
    display: flex; align-items: center;
    padding-left: 58px;
  }
  .person-name {
    color: var(--ink-light);
    font-size: 40px;
    font-weight: 500;
    letter-spacing: -0.5px;
    white-space: nowrap;
  }
  .person-name strong { font-weight: 700; }
  .panel-gap {
    position: absolute;
    top: 231px; left: 356px; width: 12px; bottom: 0;
    background: var(--divider-grey);
  }
  .contact-panel {
    position: absolute;
    top: 231px; left: 368px; right: 0; bottom: 0;
    background: var(--panel-grey);
    padding: 40px 0 0 28px;
    color: var(--ink-dark);
  }
  .job-title { font-size: 25px; font-weight: 600; margin-bottom: 20px; }
  .contact-line { font-size: 20px; font-weight: 500; margin-bottom: 22px; }

  /* Back */
  .card-back { top: 630px; height: 435px; }
  .service-map { position: absolute; inset: 0; }
  .service {
    position: absolute;
    height: 56px;
    border-radius: 8px;
    background: linear-gradient(180deg, var(--silver-top) 0%, var(--silver-mid) 55%, var(--silver-low) 100%);
    color: var(--ink-dark);
    font-family: "Roboto", sans-serif;
    font-weight: 400;
    font-size: 19px;
    line-height: 19px;
    text-align: center;
    text-transform: uppercase;
    display: flex; align-items: center; justify-content: center;
  }
  .hub-label {
    position: absolute;
    left: 0; right: 0; top: 248px;
    text-align: center;
    color: var(--ink-light);
    font-size: 23px;
    font-weight: 500;
    letter-spacing: 0.5px;
  }
</style>
</head>
<body>

  <section class="card card-front" aria-label="Business card front">
    <div class="brand">
      <span class="brand-mark" aria-hidden="true"></span>
      <h1 class="brand-name">Harborline Security<span class="brand-sub">and Surveillance</span></h1>
    </div>
    <div class="front-divider"></div>
    <div class="name-panel">
      <p class="person-name">GLEN <strong>TAVISH</strong></p>
    </div>
    <div class="panel-gap"></div>
    <div class="contact-panel">
      <p class="job-title">President</p>
      <p class="contact-line">glen@harborlinesecsys.example</p>
      <p class="contact-line">harborlinesecsys.example</p>
    </div>
  </section>

  <section class="card card-back" aria-label="Business card back: services">
    <svg class="service-map" width="762" height="435" viewBox="0 0 762 435" aria-hidden="true">
      <g fill="none" stroke="var(--dash)" stroke-width="3" stroke-dasharray="6 5">
        <polyline points="187,80 268,80 312,120"/>
        <polyline points="212,221 268,221"/>
        <polyline points="187,362 268,362 312,318"/>
        <polyline points="567,80 490,80 446,120"/>
        <polyline points="542,221 490,221"/>
        <polyline points="567,364 490,364 446,318"/>
      </g>
      <circle cx="372" cy="208" r="100" fill="var(--card-black)" stroke="var(--silver-mid)" stroke-width="5"/>
      <circle cx="372" cy="178" r="26" fill="var(--brand-blue)"/>
    </svg>
    <p class="hub-label">SERVICES</p>

    <div class="service" style="left:45px; top:52px; width:142px;">Security<br>Systems</div>
    <div class="service" style="left:47px; top:195px; width:165px;">Video<br>Surveillance</div>
    <div class="service" style="left:45px; top:332px; width:142px;">Access<br>Control</div>
    <div class="service" style="left:567px; top:54px; width:142px;">Fire Alarm<br>Systems</div>
    <div class="service" style="left:542px; top:194px; width:163px;">Network<br>Cabling</div>
    <div class="service" style="left:567px; top:336px; width:142px;">Cellular<br>Boosters</div>
  </section>

</body>
</html>
```